Find Bright Harbor Business Card and logo

We need a logo design and business card for a new consulting firm called Find Bright Harbor. We specialize in Digital Transformation of enterprises of all sizes. We help enterprises understand & significantly increase their business velocity. This requires changes in culture, organization, process and technology. We also partner with advanced technology companies to deliver tangible accelerated solutions. Methods utilized include Agile, Design Thinking, Advanced Technology Platforms (microservices, digital data, virtualization, blockchain, etc.). The final design should communicate velocity, transformation, growth and innovation.

Target Market(s)

Large Corporations and Enterprises

Contact Information for Business Card

Tagline - Shape the Coming

Logo Text

Find Bright Harbor or an initial or initials or a symbol/picture

Requirements
Must have
• Front side: Logo, name of business (Find Bright Harbor), tagline (Shape the Coming)
• Back side: First Name, Last Name, Title, Mobile Phone, Email, LinkedIn, URL (findbrightharbor.com)
Nice to have
• The design should communicate velocity, transformation, growth and/or innovation.

```html
<!DOCTYPE html>
<html lang="en">
<head>
<meta charset="UTF-8">
<title>Find Bright Harbor — Business Card</title>
<link href="https://fonts.googleapis.com/css2?family=Montserrat:wght@400;500;600;700&display=swap" rel="stylesheet">
<style>
  :root {
    --backdrop: #2a2d31;
    --card-dark: #0b0b0c;
    --card-light: #ffffff;
    --brand-red: #e8321c;
    --ink: #1c1c1c;
    --ink-soft: #444444;
    --paper-text: #f2f2f2;
    --rule-dark: #ffffff;
  }
  * { box-sizing: border-box; margin: 0; padding: 0; }
  html, body {
    width: 1200px; height: 900px; overflow: hidden;
    background: var(--backdrop);
    font-family: "Montserrat", sans-serif;
  }
  .canvas {
    position: relative; width: 1200px; height: 900px;
  }
  .card {
    position: absolute; width: 540px; height: 310px;
    border-radius: 26px;
    box-shadow: 0 14px 36px rgba(0,0,0,0.45);
  }
  .card--front {
    left: 330px; top: 110px;
    background: var(--card-dark);
    display: flex; flex-direction: column; align-items: center; justify-content: center;
  }
  .card--back {
    left: 330px; top: 480px;
    background: var(--card-light);
  }
  .brand-dot {
    width: 58px; height: 58px; border-radius: 50%;
    background: var(--brand-red);
    margin-bottom: 22px;
  }
  .brand-name {
    font-weight: 600; font-size: 19px; letter-spacing: 5px;
    text-transform: uppercase; color: var(--paper-text);
  }
  .brand-rule {
    width: 330px; height: 1px; background: var(--rule-dark);
    margin: 8px 0 7px;
  }
  .brand-tagline {
    font-weight: 400; font-size: 9px; letter-spacing: 5px;
    text-transform: uppercase; color: var(--paper-text);
  }

  .back-brand {
    position: absolute; left: 38px; top: 36px;
    display: flex; flex-direction: column; align-items: flex-start;
  }
  .back-brand .brand-dot { width: 34px; height: 34px; margin-bottom: 12px; }
  .back-brand .brand-name { font-size: 11px; letter-spacing: 3px; color: var(--ink); }
  .back-brand .brand-rule { width: 196px; background: var(--ink); margin: 5px 0 4px; }
  .back-brand .brand-tagline { font-size: 6px; letter-spacing: 3.5px; color: var(--ink-soft); }

  .person {
    position: absolute; right: 40px; top: 128px; text-align: right;
  }
  .person__name { font-weight: 600; font-size: 22px; letter-spacing: 2px; color: var(--ink); }
  .person__title { font-weight: 500; font-size: 12px; letter-spacing: 2px; color: var(--ink); margin-top: 4px; }

  .contact {
    position: absolute; left: 190px; top: 196px;
    list-style: none;
    font-size: 14px; letter-spacing: 2px; line-height: 26px; color: var(--ink);
  }
</style>
</head>
<body>
<main class="canvas">
  <section class="card card--front" aria-label="Card front">
    <div class="brand-dot"></div>
    <p class="brand-name">Find Bright Harbor</p>
    <div class="brand-rule"></div>
    <p class="brand-tagline">Shape the Coming</p>
  </section>

  <section class="card card--back" aria-label="Card back">
    <div class="back-brand">
      <div class="brand-dot"></div>
      <p class="brand-name">Find Bright Harbor</p>
      <div class="brand-rule"></div>
      <p class="brand-tagline">Shape the Coming</p>
    </div>
    <div class="person">
      <p class="person__name">John Doe</p>
      <p class="person__title">Founder</p>
    </div>
    <ul class="contact">
      <li>+11 000 0000</li>
      <li>email@findbrightharbor.com</li>
      <li>www.findbrightharbor.com</li>
    </ul>
  </section>
</main>
</body>
</html>
```